Business Card Design for Dovlan Holdings

I need a business card designed for Dovlan Holdings. I would like basic contact info and would like the card to be a bit modern but not childish. We manage several companies so it needs to look very professional. Watermark is cool and a plan logo maybe offset on the other side but I will leave the design up to you. I would like to see both color and grey scale designs. This is my first time using Sketch Harbor so hopefully we get some great results! Future projects available for the selected designer potentially.

Target Market(s)

Dovlan Holdings owns several companies serving the software, real estate and automotive industry

Industry/Entity Type

Business

Contact Information for Business Card

Gregory T. Dovlan
608.291.5537
gregory.t.dovlan@mailvista.example

Font styles to use
Serif

Requirements
Must have
• contact information listed on card details
Nice to have
• I am open to letting you use your creative mind to design the best eye catching cards.

```html
<!DOCTYPE html>
<html lang="en">
<head>
<meta charset="utf-8">
<title>Dovlan Holdings — Business Card</title>
<link rel="stylesheet" href="https://fonts.googleapis.com/css2?family=Arvo:wght@700&family=Source+Sans+3:wght@300;400;700&display=swap">
<style>
  :root {
    --page: #eceef1;
    --navy: #243f82;
    --blue: #0a8fcb;
    --mark-blue: #1d83c4;
    --silver-light: #ffffff;
    --silver-mid: #e4e5e7;
    --silver-dark: #c9cbce;
    --rule-navy: #3b3a8c;
    --white: #ffffff;
  }
  html, body {
    margin: 0;
    width: 1022px;
    height: 1200px;
    overflow: hidden;
    background: var(--page);
  }
  .card {
    position: absolute;
    left: 130px;
    width: 766px;
    display: block;
  }
  .card--front { top: 104px; height: 450px; }
  .card--back  { top: 650px; height: 445px; }
  .brand-name {
    font-family: "Arvo", Georgia, serif;
    font-weight: 700;
    fill: var(--navy);
  }
  .contact-name {
    font-family: "Source Sans 3", Arial, sans-serif;
    font-weight: 700;
    fill: var(--white);
  }
  .contact-line {
    font-family: "Source Sans 3", Arial, sans-serif;
    font-weight: 400;
    fill: var(--white);
  }
</style>
</head>
<body>

<!-- Front of card -->
<svg class="card card--front" viewBox="0 0 708 416" role="group" aria-label="Business card front">
  <defs>
    <linearGradient id="front-blue" x1="0" y1="0" x2="0" y2="1">
      <stop offset="0" stop-color="var(--navy)"/>
      <stop offset="0.3" stop-color="var(--navy)"/>
      <stop offset="1" stop-color="var(--blue)"/>
    </linearGradient>
    <linearGradient id="front-silver" x1="0" y1="0" x2="1" y2="0">
      <stop offset="0" stop-color="var(--silver-dark)"/>
      <stop offset="0.45" stop-color="var(--silver-light)"/>
      <stop offset="0.75" stop-color="var(--silver-light)"/>
      <stop offset="1" stop-color="var(--silver-dark)"/>
    </linearGradient>
  </defs>
  <rect class="card-face" width="708" height="416" fill="url(#front-silver)"/>
  <path class="band-blue" d="M0 0H708V160Q354 206 0 160Z" fill="url(#front-blue)"/>
  <path class="rule-silver" d="M0 166Q354 212 708 166" fill="none" stroke="#b9bbbe" stroke-width="5"/>
  <path class="rule-navy" d="M0 172Q354 218 708 172" fill="none" stroke="var(--rule-navy)" stroke-width="2"/>
  <circle class="brand-dot" cx="348" cy="172" r="112" fill="var(--mark-blue)"/>
  <text class="brand-name" x="354" y="346" text-anchor="middle" font-size="36">DOVLAN HOLDINGS</text>
</svg>

<!-- Back of card -->
<svg class="card card--back" viewBox="0 0 708 411" role="group" aria-label="Business card back">
  <defs>
    <linearGradient id="back-blue" x1="0" y1="0" x2="0" y2="1">
      <stop offset="0" stop-color="var(--blue)"/>
      <stop offset="0.4" stop-color="var(--navy)"/>
      <stop offset="1" stop-color="var(--navy)"/>
    </linearGradient>
    <linearGradient id="back-silver" x1="0" y1="0" x2="1" y2="0">
      <stop offset="0" stop-color="var(--silver-dark)"/>
      <stop offset="0.4" stop-color="var(--silver-light)"/>
      <stop offset="0.7" stop-color="var(--silver-light)"/>
      <stop offset="1" stop-color="var(--silver-dark)"/>
    </linearGradient>
  </defs>
  <rect class="card-face" width="708" height="411" fill="url(#back-silver)"/>
  <path class="band-blue" d="M0 196Q354 158 708 206V411H0Z" fill="url(#back-blue)"/>
  <path class="rule-navy" d="M0 186Q354 148 708 196" fill="none" stroke="var(--rule-navy)" stroke-width="2"/>
  <path class="rule-silver" d="M0 192Q354 154 708 202" fill="none" stroke="#b9bbbe" stroke-width="5"/>

  <circle class="brand-dot" cx="184" cy="102" r="41" fill="var(--mark-blue)"/>
  <text class="brand-name" x="240" y="116" font-size="29">DOVLAN HOLDINGS</text>

  <text class="contact-name" x="354" y="224" text-anchor="middle" font-size="25">Gregory T. Dovlan</text>

  <g class="icon-phone" fill="none" stroke="var(--white)" stroke-width="1.6">
    <rect x="244" y="270" width="12" height="20" rx="2"/>
    <line x1="248" y1="286" x2="252" y2="286"/>
  </g>
  <text class="contact-line" x="264" y="289" font-size="26">608.291.5537</text>

  <g class="icon-mail" fill="none" stroke="var(--white)" stroke-width="1.6">
    <rect x="122" y="314" width="24" height="16"/>
    <polyline points="122,314 134,324 146,314"/>
  </g>
  <text class="contact-line" x="154" y="329" font-size="26">gregory.t.dovlan@mailvista.example</text>
</svg>

</body>
</html>
```